Book Cover - Goals

Create book cover for book
Title: Summit Drive
Subtitle: Push Past Your Limits, Find Strength Within Yourself

See the uploaded 1st version -- I want to see different concepts -- definitely want use white space and keep a blue color similiar if not the same as the one seen in that other version and see my notes/feedback.

:

Target Market(s)

Women + Men - 35-60
Self Help + Health

Industry/Entity Type

Health And Wellness

Font styles to use
Sans Serif

Colors
0692cd
34a7d7
85cae6
cee9f5

Requirements
Must have
• Picture of father and I that can be found here:(https://files.cloudvault-share.net/folders/7K9QxRm2_41PlVnwTbZuLeHsCq3)
• and I uploaded one too (I'd like to see it with our shirts on and off)
Nice to have
• Want it to be clean
• More gender neutral -- not overly masculine or femine
• I really like these book covers - so something similair woudl be great"
• Steady Steps: The 9-Week Meal Rhythm Method
• The Quiet Harvest Plan : Retune Your Habits for Gentle Fat Burning, Steady Vigor and Lasting Stamina
• Walk Far, Feel Light for Years

```html
<!DOCTYPE html>
<html lang="en">
<head>
<meta charset="utf-8">
<title>Summit Drive — Book Cover</title>
<link rel="stylesheet" href="https://fonts.googleapis.com/css2?family=Saira+Condensed:wght@500;600;700&family=Montserrat:ital,wght@0,400;1,700&display=swap">
<style>
  :root {
    --stage: #74d0ea;
    --blue-deep: #0692cd;
    --blue-mid: #34a7d7;
    --blue-soft: #85cae6;
    --blue-pale: #cee9f5;
    --paper: #ffffff;
    --paper-shade: #e6e8ea;
    --band-ink: #e9f5fb;
  }
  html, body {
    margin: 0;
    width: 1200px;
    height: 1145px;
    overflow: hidden;
    background: var(--stage);
  }
  .cover {
    position: absolute;
    left: 230px;
    top: 48px;
    width: 740px;
    height: 1050px;
    background: linear-gradient(160deg, var(--paper) 35%, var(--paper-shade) 100%);
    overflow: hidden;
    font-family: "Saira Condensed", "Arial Narrow", sans-serif;
  }
  .title-top {
    position: absolute;
    left: 0;
    right: 0;
    top: 70px;
    margin: 0;
    text-align: center;
    font-weight: 600;
    font-size: 220px;
    line-height: 1;
    letter-spacing: 6px;
    color: var(--blue-deep);
  }
  .title-main {
    position: absolute;
    left: 0;
    right: 0;
    top: 268px;
    margin: 0;
    text-align: center;
    font-weight: 600;
    font-size: 310px;
    line-height: 1;
    letter-spacing: 8px;
    background: linear-gradient(180deg, var(--blue-soft) 0%, var(--blue-mid) 55%, var(--blue-mid) 100%);
    -webkit-background-clip: text;
    background-clip: text;
    color: transparent;
  }
  .authors-photo {
    position: absolute;
    left: 20px;
    top: 404px;
    width: 345px;
    height: 570px;
    border-radius: 40px 40px 0 0;
    background: linear-gradient(180deg, #d9a98a 0%, #c98f6d 45%, #3c6d9a 62%, #c96b5c 72%, #c99478 88%, #b98468 100%);
    opacity: 0.85;
  }
  .subtitle {
    position: absolute;
    left: 372px;
    top: 676px;
    width: 320px;
    margin: 0;
    text-align: center;
    font-family: "Montserrat", Arial, sans-serif;
    font-style: italic;
    font-weight: 700;
    font-size: 27px;
    line-height: 1.25;
    letter-spacing: 1.5px;
    color: var(--blue-deep);
  }
  .author-names {
    position: absolute;
    right: 28px;
    top: 912px;
    margin: 0;
    font-weight: 600;
    font-size: 58px;
    line-height: 1;
    letter-spacing: 1px;
    color: var(--blue-deep);
  }
  .bottom-band {
    position: absolute;
    left: 0;
    right: 0;
    bottom: 0;
    height: 76px;
    background: var(--blue-deep);
  }
  .tagline {
    position: absolute;
    right: 28px;
    top: 18px;
    margin: 0;
    font-family: "Montserrat", Arial, sans-serif;
    font-weight: 400;
    font-size: 19px;
    letter-spacing: 2px;
    text-transform: uppercase;
    color: var(--band-ink);
  }
</style>
</head>
<body>
  <main class="cover">
    <h1 class="title-top">SUMMIT</h1>
    <p class="title-main">DRIVE</p>
    <div class="bottom-band">
      <p class="tagline">The Father and Son Fitness Team</p>
    </div>
    <div class="authors-photo" role="img" aria-label="Photo of father and son standing back to back, arms crossed, in board shorts"></div>
    <p class="subtitle">Push Past Your Limits, Find Strength Within Yourself</p>
    <p class="author-names">DALE &amp; OWEN MARSH</p>
  </main>
</body>
</html>
```